Business Card & Renders for Tallow Brook Constructions

I need a minimal business card and some renders for Tallow Brook Constructions, a construction business based in Sydney Australia.

The (draft) website for the business can be seen at [login to view URL]

I have attached the front and back of the card to the contest, the logo is in the 'Card Front' file. All contact info to be included is on the 'Card Back' file along with icons used on the website for services (if you wish to use them - that is optional). Other icons should be from the Font Awesome library if you choose to use them.

1. The business card should be minimalistic, not crowded. Keep it minimal.

2. I also require a render of the logo on the business card designed showing it as embossed (raised) with a matt finish, a render of the logo showing it in an office environment and a render of the logo on a vehicle.

Any questions let me know. Good luck!

Cheers - Ned

```html
<!DOCTYPE html>
<html lang="en">
<head>
<meta charset="utf-8">
<title>Tallow Brook Constructions – Business Card</title>
<link rel="stylesheet" href="https://fonts.googleapis.com/css2?family=Federo&family=DM+Serif+Display&family=Arimo:wght@400;600&display=swap">
<style>
  :root {
    --backdrop: #e4e2df;
    --card-cream: #f8f4f0;
    --card-white: #fbfaf8;
    --ink-dark: #3a3836;
    --ink-mid: #5b5855;
    --rule-gold: #9a7a4a;
    --band-dark: #3b3a38;
    --band-mid: #4b4a48;
    --text-light: #ffffff;
    --badge-line: #c9c2bb;
    --badge-fill: #f1ede9;
    --badge-text: #a79f98;
    --photo-wood: #9a5f38;
    --photo-wood-dark: #6b3f24;
    --photo-green: #5d7a45;
  }
  * { box-sizing: border-box; margin: 0; padding: 0; }
  html, body { width: 1200px; height: 780px; overflow: hidden; }
  body { background: var(--backdrop); position: relative; font-family: "Arimo", sans-serif; }

  .card {
    position: absolute;
    width: 560px;
    height: 320px;
    box-shadow: 0 10px 28px rgba(0,0,0,0.18);
    overflow: hidden;
  }

  /* ---------- Front ---------- */
  .card-front {
    left: 60px; top: 60px;
    background: var(--card-cream);
    display: flex;
    align-items: center;
    padding: 0 40px 0 62px;
    gap: 34px;
  }
  .front-mark {
    width: 132px; height: 132px;
    border-radius: 50%;
    background: var(--ink-dark);
    flex-shrink: 0;
  }
  .front-wordmark { flex: 1; text-align: center; }
  .front-name {
    font-family: "Federo", sans-serif;
    color: var(--ink-dark);
    text-transform: uppercase;
    line-height: 1;
  }
  .front-name .line-1 { display: block; font-size: 38px; letter-spacing: 1px; padding-bottom: 10px; }
  .front-name .line-2 {
    display: block; font-size: 34px; letter-spacing: 0.5px;
    border-top: 2px solid var(--rule-gold);
    border-bottom: 2px solid var(--rule-gold);
    padding: 10px 0;
  }

  /* ---------- Back ---------- */
  .card-back {
    left: 580px; top: 400px;
    background: var(--card-white);
  }
  .back-photo {
    position: absolute; left: 0; top: 0;
    width: 100%; height: 190px;
    background:
      linear-gradient(100deg, var(--photo-wood) 0%, var(--photo-wood-dark) 42%, var(--photo-wood) 58%, var(--photo-green) 78%, #3f5a30 100%);
  }
  .contact-panel {
    position: absolute; right: 0; top: 100px;
    width: 320px; height: 140px;
    background: rgba(59,58,56,0.92);
  }
  .contact-list { list-style: none; padding: 8px 0 0 0; }
  .contact-item {
    display: flex; align-items: center;
    height: 40px;
    color: var(--text-light);
    font-size: 12.5px;
  }
  .contact-item .icon {
    width: 36px; height: 100%;
    display: flex; align-items: center; justify-content: center;
    border-right: 1px solid rgba(255,255,255,0.35);
    margin-right: 12px;
  }
  .contact-item.phone { font-size: 15px; }

  .name-band {
    position: absolute; left: 0; top: 170px;
    width: 240px; height: 70px;
    background: var(--band-mid);
    color: var(--text-light);
    padding: 12px 0 0 24px;
  }
  .name-band::before {
    content: ""; position: absolute; top: -10px; left: 102px;
    border-left: 10px solid transparent; border-right: 10px solid transparent;
    border-bottom: 10px solid var(--band-mid);
  }
  .person-name { font-family: "DM Serif Display", serif; font-size: 25px; line-height: 1.05; }
  .person-title { font-family: "DM Serif Display", serif; font-size: 16px; padding-left: 34px; }

  .back-footer {
    position: absolute; left: 0; top: 240px;
    width: 100%; height: 80px;
    display: flex; align-items: center;
    padding: 0 24px 0 78px;
  }
  .footer-brand { display: flex; align-items: center; gap: 10px; }
  .footer-brand .mark { width: 34px; height: 34px; border-radius: 50%; background: var(--ink-mid); }
  .footer-brand .name {
    font-family: "Federo", sans-serif; color: var(--ink-mid);
    font-size: 12px; line-height: 1.2; text-transform: uppercase; text-align: center;
  }
  .service-badges { margin-left: auto; display: flex; gap: 14px; margin-top: -16px; }
  .badge {
    width: 58px; height: 58px; border-radius: 50%;
    border: 2px solid var(--badge-line);
    background: var(--badge-fill);
    display: flex; align-items: center; justify-content: center; text-align: center;
    color: var(--badge-text);
    font-size: 7px; letter-spacing: 0.5px; text-transform: uppercase; line-height: 1.3;
  }
</style>
</head>
<body>

  <section class="card card-front" aria-label="Business card front">
    <div class="front-mark"></div>
    <div class="front-wordmark">
      <h1 class="front-name">
        <span class="line-1">Tallow Brook</span>
        <span class="line-2">Constructions</span>
      </h1>
    </div>
  </section>

  <section class="card card-back" aria-label="Business card back">
    <div class="back-photo" role="img" aria-label="Photograph of a timber deck with glass balustrade overlooking a leafy garden"></div>

    <div class="contact-panel">
      <ul class="contact-list">
        <li class="contact-item phone">
          <span class="icon">
            <svg width="16" height="16" viewBox="0 0 24 24" fill="#fff"><path d="M6.6 10.8a15.1 15.1 0 0 0 6.6 6.6l2.2-2.2a1 1 0 0 1 1-.25 11.4 11.4 0 0 0 3.6.57 1 1 0 0 1 1 1V20a1 1 0 0 1-1 1A17 17 0 0 1 3 4a1 1 0 0 1 1-1h3.5a1 1 0 0 1 1 1c0 1.25.2 2.45.57 3.57a1 1 0 0 1-.25 1z"/></svg>
          </span>
          940 – 612 – 4087
        </li>
        <li class="contact-item">
          <span class="icon">
            <svg width="16" height="16" viewBox="0 0 24 24" fill="none" stroke="#fff" stroke-width="1.8"><circle cx="12" cy="12" r="9"/><path d="M3 12h18M12 3c3 3.2 3 14.8 0 18M12 3c-3 3.2-3 14.8 0 18"/></svg>
          </span>
          tallowbrookconstructions.com.au
        </li>
        <li class="contact-item">
          <span class="icon">
            <svg width="16" height="16" viewBox="0 0 24 24" fill="none" stroke="#fff" stroke-width="1.8"><rect x="3" y="6" width="18" height="12" rx="1"/><path d="M3 7l9 6 9-6"/></svg>
          </span>
          sales@tallowbrookconstructions.com.au
        </li>
      </ul>
    </div>

    <div class="name-band">
      <p class="person-name">Owen Hartley</p>
      <p class="person-title">Managing Director</p>
    </div>

    <div class="back-footer">
      <div class="footer-brand">
        <span class="mark"></span>
        <span class="name">Tallow Brook<br>Constructions</span>
      </div>
      <div class="service-badges">
        <span class="badge">Contact<br>&amp;<br>Quote</span>
        <span class="badge">Services</span>
        <span class="badge">Projects</span>
      </div>
    </div>
  </section>

</body>
</html>
```